Brightfield Co Trade Show Flyer

We need a brochure design (8.5 x 11) Info in the design (refer to rough draft I drew on Paper): "#1 selling tool to aquire new franchisees has been video testimonials" - Martin L. Crowe, C.E.O Tovik Smoothie Franchise Testimonials - Let your franchisees do the selling for you. Franchisee testimonial: $10,000 / per Franchisee Includes: • 2 minute Video • 1 minute add for your franchise's location • Concept creation • Communication with franchisee • Travel to their location • All rental equipment • 1 round of corrections • Animated logo • Licensed music ******* For 25% Discount section (next to middle box), please put the "Outlet Summit Logo" Great to use on all your social media (USE logos and icons) • Website • Vidstream • Worklink • Friendnet • Lenso • Chirpline • Phone calls • Emails • In person meetings Some of our clients: (use the logos I uploaded - in round boxes as in draft) LOGO (Brightfield Franchise Testimonial) www.brightfieldvoices.example (866) 555-0172

Target Market(s)

Franchise owners

Colors

Designer to choose colors to be used in the design.

Requirements

```html
<!DOCTYPE html>
<html lang="en">
<head>
<meta charset="utf-8">
<title>Brightfield Co Trade Show Flyer</title>
<link rel="stylesheet" href="https://fonts.googleapis.com/css2?family=Lato:ital,wght@0,400;0,700;0,900;1,400&family=Montserrat:wght@400&family=Oswald:wght@700&family=Lobster&display=swap">
<style>
:root{
  --navy:#1c2740;
  --white:#ffffff;
  --orange:#f7931e;
  --yellow:#ffd400;
  --amber:#f7a11a;
  --red:#e8141c;
  --green:#0a9d6e;
  --backdrop:#d6d6d6;
  --ink:#111111;
}
*{margin:0;padding:0;box-sizing:border-box}
html,body{width:1200px;height:1200px;overflow:hidden;background:var(--backdrop)}
.flyer{position:absolute;left:169px;top:33px;width:861px;height:1134px;background:var(--navy);overflow:hidden;font-family:"Lato",sans-serif;color:var(--white)}
.abs{position:absolute}
.quote-box{left:76px;top:49px;width:729px;height:65px;border:1px solid var(--white);border-bottom:none}
.quote-box::before,.quote-box::after{content:"";position:absolute;bottom:0;height:1px;background:var(--white)}
.quote-box::before{left:0;width:195px}
.quote-box::after{right:0;width:195px}
.quote-text{left:0;width:861px;top:58px;text-align:center;font-style:italic;font-size:39px;line-height:1}
.quote-credit{left:0;width:861px;top:102px;text-align:center;font-style:italic;font-size:20px;line-height:1.2}
.headline{left:0;width:861px;text-align:center;font-family:"Montserrat",sans-serif;font-weight:400;font-size:88px;line-height:1;color:transparent;-webkit-text-stroke:2px var(--white);letter-spacing:0}
.headline.one{top:149px}
.headline.two{top:231px}
.tagline{left:0;width:861px;top:330px;text-align:center;font-size:34px;line-height:1.2;color:var(--amber)}
.badge{left:41px;top:379px;width:320px;height:320px}
.badge-text{left:41px;top:379px;width:320px;text-align:center;color:var(--red)}
.badge-pct{position:absolute;left:0;width:320px;top:28px;font-family:"Lobster",sans-serif;font-size:92px;line-height:1;transform:rotate(-6deg)}
.badge-word{position:absolute;left:0;width:320px;top:118px;font-family:"Oswald",sans-serif;font-size:64px;line-height:1;transform:rotate(-4deg)}
.badge-for{position:absolute;left:0;width:320px;top:190px;font-style:italic;font-size:20px;color:var(--navy)}
.partner{position:absolute;left:88px;top:220px;display:flex;align-items:center;gap:6px;font-weight:700;font-size:17px;color:var(--navy)}
.partner i{display:block;width:16px;height:16px;background:var(--green)}
.price-box{left:381px;top:384px;width:412px;height:315px;border:1px solid var(--white);border-radius:14px}
.price-title{position:absolute;left:0;width:412px;top:12px;text-align:center;font-size:30px;line-height:1.25;font-weight:400}
.price-list{position:absolute;left:22px;top:88px;list-style:none;font-size:19.5px;line-height:24.2px}
.price-list li::before{content:"";display:inline-block;width:8px;height:8px;border-radius:50%;background:var(--amber);margin-right:10px;vertical-align:middle}
.usage{left:0;width:861px;top:722px;text-align:center;font-size:25px}
.channels{left:208px;top:765px;display:flex;gap:17px}
.channel{width:44px;height:44px;border-radius:50%;border:1.5px solid var(--channel);display:flex;align-items:center;justify-content:center;font-size:8px;font-weight:700;color:var(--channel);text-align:center;line-height:1}
.trusted{left:0;width:861px;top:845px;text-align:center;font-size:25px}
.clients{left:204px;top:888px;display:flex;gap:13px}
.client{width:68px;height:68px;border-radius:50%;background:var(--white);color:var(--navy);display:flex;align-items:center;justify-content:center;text-align:center;font-size:10px;font-weight:700;line-height:1.1;padding:4px}
.wave{left:0;top:0;width:861px;height:1134px}
.brand{left:77px;top:1060px;color:var(--ink)}
.brand-name{font-weight:900;font-size:34px;letter-spacing:1px;line-height:1}
.brand-sub{font-weight:700;font-size:9px;margin-left:27px;margin-top:3px}
.contact{right:23px;top:1078px;color:var(--ink);text-align:right;font-size:19px;line-height:22px}
.contact-line{display:flex;align-items:center;justify-content:flex-end;gap:7px}
</style>
</head>
<body>
<main class="flyer">
  <div class="abs quote-box"></div>
  <p class="abs quote-text">"#1 selling tool to aquire new franchisees "</p>
  <p class="abs quote-credit">- Martin L. Crowe, C.E.O Tovik Smoothie</p>

  <h1 class="abs headline one">FRANCHISE</h1>
  <h1 class="abs headline two">TESTIMONIALS</h1>
  <p class="abs tagline">Let your franchisees do the selling for you.</p>

  <svg class="abs badge" viewBox="0 0 320 320" aria-hidden="true">
    <defs><linearGradient id="burst" x1="0" x2="1"><stop offset="0" stop-color="#f7931e"/><stop offset="1" stop-color="#ffd400"/></linearGradient></defs>
    <polygon fill="url(#burst)" points="317,160 280,184 305,220 261,228 271,271 228,261 220,305 184,280 160,317 136,280 100,305 92,261 49,271 59,228 15,220 40,184 3,160 40,136 15,100 59,92 49,49 92,59 100,15 136,40 160,3 184,40 220,15 228,59 271,49 261,92 305,100 280,136"/>
  </svg>
  <div class="abs badge-text">
    <div class="badge-pct">25%</div>
    <div class="badge-word">DISCOUNT</div>
    <div class="badge-for">for</div>
    <div class="partner"><i></i>Outlet Summit</div>
  </div>

  <section class="abs price-box">
    <h2 class="price-title">$10,000 / per Franchisee<br>Includes:</h2>
    <ul class="price-list">
      <li>2 minute Video</li>
      <li>1 minute add for your franchise's location</li>
      <li>Concept creation</li>
      <li>Communication with franchisee</li>
      <li>Travel to their location</li>
      <li>All rental equipment</li>
      <li>1 round of corrections</li>
      <li>Animated logo</li>
      <li>Licensed music</li>
    </ul>
  </section>

  <p class="abs usage">Use your testimonial everywhere.</p>
  <div class="abs channels">
    <div class="channel" style="--channel:#29a9e1">Chirpline</div>
    <div class="channel" style="--channel:#3b5998">Friendnet</div>
    <div class="channel" style="--channel:#f58529">Lenso</div>
    <div class="channel" style="--channel:#e62117">Vidstream</div>
    <div class="channel" style="--channel:#0e76a8">Worklink</div>
    <div class="channel" style="--channel:#e62117"><svg width="22" height="16" viewBox="0 0 22 16"><rect x="1" y="1" width="20" height="14" fill="#e62117"/><path d="M1 1l10 8 10-8" stroke="#fff" stroke-width="1.5" fill="none"/></svg></div>
    <div class="channel" style="--channel:#ffffff"><svg width="26" height="26" viewBox="0 0 26 26" fill="none" stroke="#fff" stroke-width="1.5"><circle cx="13" cy="13" r="11"/><ellipse cx="13" cy="13" rx="5" ry="11"/><path d="M2 13h22"/></svg></div>
    <div class="channel" style="--channel:#1e90d6"><svg width="20" height="20" viewBox="0 0 24 24"><path fill="#1e90d6" d="M6.6 10.8a15 15 0 006.6 6.6l2.2-2.2c.3-.3.7-.4 1-.2 1.1.4 2.3.6 3.6.6.6 0 1 .4 1 1V20c0 .6-.4 1-1 1A17 17 0 013 4c0-.6.4-1 1-1h3.5c.6 0 1 .4 1 1 0 1.3.2 2.5.6 3.6.1.3 0 .7-.2 1z"/></svg></div>
  </div>

  <p class="abs trusted">TRUSTED BY:</p>
  <div class="abs clients">
    <div class="client">Creamery Lane</div>
    <div class="client">Corner Daily</div>
    <div class="client">Tovik Smoothie</div>
    <div class="client">Tidewell Cleaning</div>
    <div class="client">Gearline Auto</div>
    <div class="client">Outlet Summit</div>
  </div>

  <svg class="abs wave" viewBox="0 0 1230 1620" preserveAspectRatio="none" aria-hidden="true">
    <defs>
      <linearGradient id="sweep" x1="0" x2="1"><stop offset="0" stop-color="#f7931e"/><stop offset="1" stop-color="#ffd400"/></linearGradient>
    </defs>
    <path fill="url(#sweep)" d="M1230 1270 C1170 1400 1050 1500 880 1500 C940 1490 1120 1440 1230 1330 Z"/>
    <path fill="#ffffff" d="M0 1432 C260 1350 560 1360 850 1470 C960 1510 1100 1505 1230 1420 L1230 1620 L0 1620 Z"/>
    <path fill="url(#sweep)" d="M0 1412 C250 1360 420 1370 560 1400 C320 1390 130 1400 0 1432 Z"/>
    <path fill="url(#sweep)" d="M420 1400 C600 1400 700 1470 780 1530 C820 1570 840 1600 860 1620 L1230 1620 C1160 1610 1000 1600 900 1540 C780 1470 640 1410 420 1400 Z"/>
  </svg>

  <div class="abs brand">
    <div class="brand-name">BRIGHTFIELD</div>
    <div class="brand-sub">FRANCHISE TESTIMONIALS –</div>
  </div>

  <div class="abs contact">
    <div class="contact-line"><svg width="16" height="16" viewBox="0 0 24 24"><path fill="#111" d="M6.6 10.8a15 15 0 006.6 6.6l2.2-2.2c.3-.3.7-.4 1-.2 1.1.4 2.3.6 3.6.6.6 0 1 .4 1 1V20c0 .6-.4 1-1 1A17 17 0 013 4c0-.6.4-1 1-1h3.5c.6 0 1 .4 1 1 0 1.3.2 2.5.6 3.6.1.3 0 .7-.2 1z"/></svg>(866) 555-0172</div>
    <div class="contact-line" style="font-size:17px"><svg width="16" height="16" viewBox="0 0 26 26" fill="none" stroke="#111" stroke-width="1.5"><circle cx="13" cy="13" r="11"/><ellipse cx="13" cy="13" rx="5" ry="11"/><path d="M2 13h22"/></svg>www.brightfieldvoices.example</div>
  </div>
</main>
</body>
</html>
```